Comic, writer, and entrepreneur based in Los Angeles, CA

UPDATED BRIEF:

Need a PROFESSIONAL yet simultaneously sexy business card that will inspire those to go to my social media accounts and follow me.

Need all of my social media (logos on card, please) As well as my picture, which I will provide.

If there is a way where you could scan the business card from your phone and it would take you to the social media accounts that would be great too!

My goal is to get a comedy writing job at the Nightly Desk or WLR and also go on Pelican Pond once my app is fully functional and created.

But the business card is just something to give people when I am making connections in both the entrepreneurial world as well as the comedy world so it has to help me stand out in that way :).

#: 417-552-8904
Email: kbellin@mx.ovrk.edu
Pictogram: Rosalind_Q.K
Chirpr: @ThePalermoNotes
Craftlo: Rosa’s Clever Tops (website: https://www.craftlo-example.com/shop/RosasTp?ref=pr_shop_more)
VidStream: The Gagmistress (website: https://www.vidstream-example.com/channel/QRpLwVn4kZ-mTHbyqo8erxt7B )
Friendlink: /rosalind.bellin.71924
Website App: WarmFixerFolk.example (app in progress. Need emails to make a prototype.)

Target Market(s)

Talent agents needing TV writers and TV comedy personalities. Investors for my app.

Industry/Entity Type

Tv

Contact Information for Business Card

Can be double or single sided, whichever looks best. Green is my favorite color but I am open to anything. Maybe silver and green?! Just make it classy and sexy.

Colors

Designer to choose colors to be used in the design.

Requirements
Must have
• Chirpr: ThePalermoNotes
• Pictogram: Rosalind_q.k
• Vidstream: The Gagmistress
• Email: kbellin@mx.ovrk.edu
• Phone: 417-552-8904
• writer, comic, entrepreneur--or--comedy writer and entrepeneur
Nice to have
• Make me standout. I'm a star ;-). Please check out my social media for files or ideas. Thanks.

```html
<!DOCTYPE html>
<html lang="en">
<head>
<meta charset="UTF-8">
<title>Elara Vantress — Business Card</title>
<link href="https://fonts.googleapis.com/css2?family=Work+Sans:wght@400;500;600&family=Oswald:wght@500&family=Roboto:wght@500;700&display=swap" rel="stylesheet">
<style>
  :root {
    --stage: #2a2a2a;
    --card: #ffffff;
    --pink: #e2399a;
    --pink-soft: #f6c6e0;
    --ink: #4a4a4a;
    --ink-soft: #6b6b6b;
  }
  * { box-sizing: border-box; margin: 0; padding: 0; }
  html, body {
    width: 1200px; height: 900px; overflow: hidden;
    background: var(--stage);
  }
  .stage {
    width: 1200px; height: 900px;
    display: flex; flex-direction: column; align-items: center; justify-content: center;
    gap: 34px;
  }
  .card {
    position: relative;
    width: 700px; height: 400px;
    background: var(--card);
    border-radius: 22px;
    overflow: hidden;
  }

  /* Front */
  .card-front {
    display: flex; flex-direction: column; align-items: center; justify-content: center;
  }
  .front-name {
    font-family: 'Work Sans', sans-serif;
    font-weight: 600;
    font-size: 40px;
    letter-spacing: 1px;
    color: var(--pink);
    line-height: 1;
  }
  .front-roles {
    margin-top: 8px;
    font-family: 'Work Sans', sans-serif;
    font-weight: 400;
    font-size: 15px;
    color: var(--pink);
  }

  /* Back */
  .portrait {
    position: absolute; left: 70px; top: 52px;
    width: 128px; height: 128px;
    border-radius: 50%;
    background: linear-gradient(160deg, var(--pink-soft), #d9d9d9);
    border: 3px solid var(--pink);
  }
  .identity {
    position: absolute; right: 52px; top: 100px;
    text-align: right;
  }
  .back-name {
    font-family: 'Oswald', sans-serif;
    font-weight: 500;
    font-size: 40px;
    letter-spacing: 0.5px;
    color: var(--pink);
    line-height: 1;
  }
  .back-roles {
    margin-top: 4px;
    font-family: 'Roboto', sans-serif;
    font-weight: 700;
    font-size: 15px;
    letter-spacing: 0.5px;
    color: var(--pink);
  }
  .address {
    margin-top: 14px;
    font-family: 'Work Sans', sans-serif;
    font-size: 16px;
    line-height: 1.4;
    color: var(--ink-soft);
  }
  .address .label, .contact .label, .social .label { color: var(--ink); font-weight: 500; }

  .contact {
    position: absolute; left: 70px; top: 226px;
    font-family: 'Work Sans', sans-serif;
    font-size: 17px;
    line-height: 1.45;
    color: var(--ink-soft);
  }
  .edge-tab {
    position: absolute; left: 0; top: 232px;
    width: 14px; height: 30px;
    background: var(--pink);
  }

  .socials {
    position: absolute; left: 70px; top: 296px;
    display: flex; flex-direction: column; gap: 4px;
    list-style: none;
    font-family: 'Work Sans', sans-serif;
    font-size: 14px;
    color: var(--ink-soft);
  }
  .social { display: flex; align-items: center; gap: 8px; }
  .social-dot {
    width: 8px; height: 8px; border-radius: 50%;
    background: var(--pink);
  }

  .base-band {
    position: absolute; left: 0; bottom: 0;
    width: 700px; height: 40px;
  }
</style>
</head>
<body>
<main class="stage">
  <section class="card card-front" aria-label="Card front">
    <h1 class="front-name">ELARA VANTRESS</h1>
    <p class="front-roles">Write - Comic -Entrepreneur</p>
  </section>

  <section class="card card-back" aria-label="Card back">
    <div class="portrait" role="img" aria-label="Portrait photo of Elara Vantress"></div>

    <div class="identity">
      <h2 class="back-name">ELARA VANTRESS</h2>
      <p class="back-roles">WRITER, COMIC, ENTREPRENEUR</p>
      <p class="address"><span class="label">A :</span> Suite 418,<br>27 Harbourview Lane Glenmore NSW 2164</p>
    </div>

    <span class="edge-tab"></span>
    <div class="contact">
      <p><span class="label">Phone:</span> 417-552-8904</p>
      <p><span class="label">Email:</span> kbellin@mx.ovrk.edu</p>
    </div>

    <ul class="socials">
      <li class="social"><span class="social-dot"></span><span class="label">Chirpr:</span> @ThePalermoNotes</li>
      <li class="social"><span class="social-dot"></span><span class="label">Pictogram:</span> Rosalind_q.k</li>
      <li class="social"><span class="social-dot"></span><span class="label">Vidstream:</span> The Gagmistress</li>
    </ul>

    <svg class="base-band" viewBox="0 0 700 40" aria-hidden="true">
      <polygon points="0,30 452,30 446,40 0,40" fill="var(--pink)"/>
      <polygon points="460,22 700,2 700,40 450,40" fill="var(--pink)"/>
    </svg>
  </section>
</main>
</body>
</html>
```